Brightpath Medical Exercise, LLC specializes in post rehab medical exercise for clients who have been discharged from physical therapy and/or other medical services and are in need of continued cardiovascular, strength, flexibility, endurance training and management of their medical conditions. We strive to bridge the gap between healthcare and fitness by staying in communication with the referring physician and /or physical therapist with updated progress notes to follow each clients progression, making sure each client is appropriate for exercise and identifying any red flags throughout the initial assessment and screening of the client, and referring those clients back to the physician and/or therapist when necessary.
Colors
Designer to choose colors to be used in the design.
Requirements
Must have
- Pictures of a trainer working with a client one on one during exercise, and group exercise
Nice to have
- Pictures that portray the bridge between healthcare and fitness
Should not have
- Cursive writing

```html
<!DOCTYPE html>
<html lang="en">
<head>
<meta charset="utf-8">
<title>Brightpath Medical Exercise – Rack Card</title>
<link href="https://fonts.googleapis.com/css2?family=Montserrat:wght@400;500;600;700;800&family=Oswald:wght@400;500&display=swap" rel="stylesheet">
<style>
  :root{
    --red:#ef4a48;
    --red-deep:#e23b3a;
    --dark:#2b2b2b;
    --ink:#333333;
    --grey-band:#e9e9e9;
    --white:#ffffff;
    --canvas:#ecebe8;
  }
  *{box-sizing:border-box;margin:0;padding:0}
  html,body{width:733px;height:1200px;overflow:hidden;background:var(--canvas)}
  body{position:relative;font-family:"Montserrat",sans-serif;color:var(--ink)}
  .card{position:absolute;top:219px;width:340px;height:761px;background:var(--white);overflow:hidden;box-shadow:0 2px 8px rgba(0,0,0,.18)}
  .card--front{left:18px}
  .card--back{left:375px}
  .abs{position:absolute}

  /* front */
  .brand{left:0;right:0;top:20px;text-align:center}
  .brand__mark{width:96px;height:96px;border-radius:50%;border:5px solid var(--red);margin:0 auto 12px}
  .brand__name{font-weight:800;font-size:10px;line-height:12px;color:var(--dark);letter-spacing:.2px;text-transform:uppercase}
  .hero{left:0;top:170px}
  .badge{left:96px;top:473px;width:148px;height:148px;border-radius:50%;background:var(--dark);border:4px solid #d8d8d8;color:var(--white);text-align:center;padding-top:30px}
  .badge__name{color:var(--red);font-weight:800;font-size:11px;line-height:13px;text-transform:uppercase}
  .badge__quote{color:var(--red);font-weight:800;font-size:16px;line-height:12px;margin-top:3px}
  .badge__tag{font-weight:700;font-size:8.6px;line-height:11px;padding:0 12px}
  .pill-services{left:39px;top:632px;width:262px;height:27px;border-radius:14px;background:var(--dark);border:2px solid var(--red);color:var(--white);font-weight:600;font-size:13px;line-height:23px;text-align:center;text-transform:uppercase}
  .pill-services em{font-style:normal;color:var(--red)}
  .services{left:0;right:0;top:668px;text-align:center;font-size:10px;line-height:15px;color:var(--ink)}

  .footer{left:0;right:0;bottom:0;height:31px;background:var(--red);color:var(--white);display:flex;align-items:center;justify-content:center;gap:8px;font-size:10px}
  .footer__icon{width:16px;height:16px;flex:none}
  .footer__sep{width:1px;height:18px;background:var(--white);margin:0 4px}
  .footer__phone{font-weight:700;font-size:13.5px}

  /* back */
  .photo-top{left:0;top:0}
  .quote{left:23px;top:316px;width:292px;height:68px;border:1px solid var(--red);text-align:center;padding-top:14px}
  .quote__mark{position:absolute;left:0;right:0;color:var(--red);font-weight:800;font-size:20px;line-height:14px;background:transparent}
  .quote__mark--open{top:-10px}
  .quote__mark--close{bottom:-14px}
  .quote__mark span{background:var(--white);padding:0 4px}
  .quote__text{font-weight:700;font-size:10.8px;line-height:13.5px;color:var(--ink)}
  .quote__by{font-size:10px;line-height:14px;color:var(--red);font-weight:500}
  .grey-band{left:0;right:0;top:418px;height:50px;background:var(--grey-band)}
  .pill-offer{left:96px;top:405px;width:158px;height:28px;border-radius:14px;background:var(--red);color:var(--white);font-weight:800;font-size:19px;line-height:28px;text-align:center}
  .offer-sub{left:0;right:0;top:438px;text-align:center;font-family:"Oswald",sans-serif;font-weight:500;font-size:13.6px;color:var(--ink)}
  .conditions{left:0;right:0;top:469px;height:261px;background:linear-gradient(180deg,#4a4a4a 0%,#2e2e2e 60%,#262626 100%);display:flex;padding:24px 0 0 14px}
  .conditions ul{list-style:none;width:160px}
  .conditions li{position:relative;padding-left:10px;color:var(--white);font-size:10.3px;line-height:15.2px;white-space:nowrap}
  .conditions li::before{content:"";position:absolute;left:0;top:6px;width:4px;height:4px;border-radius:50%;background:var(--red)}
</style>
</head>
<body>

<section class="card card--front">
  <div class="abs brand">
    <div class="brand__mark"></div>
    <div class="brand__name">Brightpath<br>Medical Exercise</div>
  </div>

  <svg class="abs hero" width="340" height="390" viewBox="0 0 340 390">
    <defs>
      <linearGradient id="heroTone" x1="0" y1="0" x2="1" y2="1">
        <stop offset="0" stop-color="#d9dde2"/>
        <stop offset=".45" stop-color="#8a8f98"/>
        <stop offset="1" stop-color="#244e9a"/>
      </linearGradient>
    </defs>
    <path d="M0,70 Q170,-15 340,70 L340,330 Q170,405 0,330 Z" fill="url(#heroTone)" role="img" aria-label="Photo of a smiling older man exercising with a gym ring"/>
    <path d="M0,58 Q170,-30 340,58 L340,76 Q170,5 0,76 Z" fill="var(--red)"/>
    <path d="M0,320 Q170,395 340,320 L340,336 Q170,418 0,336 Z" fill="var(--red)"/>
  </svg>

  <div class="abs badge">
    <div class="badge__name">Brightpath<br>Medical Exercise, LLC</div>
    <div class="badge__quote">&ldquo;</div>
    <div class="badge__tag">Getting You Back To Function As Quickly And Safely As Possible</div>
    <div class="badge__quote">&rdquo;</div>
  </div>

  <div class="abs pill-services">Our <em>Products</em> and <em>Services</em></div>
  <div class="abs services">
    <p>Initial Assessment and Functional Screening</p>
    <p>One-On-One supervised post rehab exercise</p>
    <p>Online consultation with individualized home exercise program</p>
  </div>

  <footer class="abs footer">
    <svg class="footer__icon" viewBox="0 0 16 16" fill="none" stroke="#fff" stroke-width="1.2"><circle cx="8" cy="8" r="7"/><ellipse cx="8" cy="8" rx="3" ry="7"/><path d="M1 8h14M2.5 4.5h11M2.5 11.5h11"/></svg>
    <span>www.brightpathmedex.com</span>
    <span class="footer__sep"></span>
    <svg class="footer__icon" viewBox="0 0 16 16" fill="#fff"><path d="M4 1.5l2.2 3-1.3 1.5c.8 1.8 2.3 3.3 4.1 4.1l1.5-1.3 3 2.2-1.2 2.5C7 13.2 2.8 9 1.5 2.7z"/></svg>
    <span class="footer__phone">5550142736</span>
  </footer>
</section>

<section class="card card--back">
  <svg class="abs photo-top" width="340" height="300" viewBox="0 0 340 300">
    <defs>
      <linearGradient id="deckTone" x1="0" y1="0" x2="0" y2="1">
        <stop offset="0" stop-color="#3d3a33"/>
        <stop offset=".25" stop-color="#8b8272"/>
        <stop offset="1" stop-color="#c4b9a8"/>
      </linearGradient>
    </defs>
    <path d="M0,0 H340 V210 Q170,305 0,210 Z" fill="url(#deckTone)" role="img" aria-label="Photo of blue dumbbells and a water bottle on a wooden deck"/>
    <path d="M0,190 Q170,300 340,190 L340,205 Q170,330 0,205 Z" fill="var(--red)"/>
  </svg>

  <div class="abs quote">
    <div class="quote__mark quote__mark--open"><span>&ldquo;</span></div>
    <p class="quote__text">Exercise is the key to long-term management<br>of most medical conditions</p>
    <p class="quote__by">Daniel R Hale, PhD, PT</p>
    <div class="quote__mark quote__mark--close"><span>&rdquo;</span></div>
  </div>

  <div class="abs grey-band"></div>
  <div class="abs pill-offer">WE OFFER</div>
  <div class="abs offer-sub">Management of The Following Conditions and More</div>

  <div class="abs conditions">
    <ul>
      <li>Diabetes</li>
      <li>Hypertension</li>
      <li>ACL Rupture</li>
      <li>Ankle Fracture</li>
      <li>Bicipital Tendonitis</li>
      <li>Total Hip Replacement</li>
      <li>Total Knee Replacement</li>
      <li>Spinal Stenosis</li>
      <li>Multiple Sclerosis</li>
      <li>Shoulder Dislocation</li>
      <li>Scoliosis</li>
      <li>Osteoporosis</li>
      <li>Osteoarthritis</li>
      <li>Cervical disc herniation</li>
    </ul>
    <ul>
      <li>AC Joint Separation</li>
      <li>Fibromyalgia</li>
      <li>SpondylothesisParkinson's</li>
      <li>DiseaseTibial Plateau Fracture</li>
      <li>TennisElbow/Golfer's Elbow</li>
      <li>Carpal Tunnel Syndrome</li>
      <li>Total Shoulder Replacement</li>
      <li>Bicipital Tendonitis</li>
      <li>Patello-Femoral Syndrome</li>
      <li>Rotator Cuff Syndrome</li>
      <li>Cervical Strain</li>
      <li>Impingement Syndrome</li>
      <li>Laminectomy</li>
    </ul>
  </div>

  <footer class="abs footer">
    <svg class="footer__icon" viewBox="0 0 16 16" fill="none" stroke="#fff" stroke-width="1.2"><circle cx="8" cy="8" r="7"/><ellipse cx="8" cy="8" rx="3" ry="7"/><path d="M1 8h14M2.5 4.5h11M2.5 11.5h11"/></svg>
    <span>www.brightpathmedex.com</span>
    <span class="footer__sep"></span>
    <svg class="footer__icon" viewBox="0 0 16 16" fill="#fff"><path d="M4 1.5l2.2 3-1.3 1.5c.8 1.8 2.3 3.3 4.1 4.1l1.5-1.3 3 2.2-1.2 2.5C7 13.2 2.8 9 1.5 2.7z"/></svg>
    <span class="footer__phone">5550142736</span>
  </footer>
</section>

</body>
</html>
```